New shirt company looking for a fun and edgy online retail website design

We're a new company looking for a simple yet attractive website to sell shirts/tops to a mostly younger female audience. Our name is Tavi Shirt Co. and the PlanHerd logo is uploaded. We're thinking a home page, three separate pages for our shirt "collections", and a contact page/cart page for a grand total of 5 pages. We'd like the website to be coded, easy for the consumer to navigate/shop/checkout, and easy to link to various social media platforms and online websites. For colors, we're aiming for various blues, light grey, and maybe tan/khaki. Our goal is to launch with approximately 20-30 tops/shirts (or 7-10) per page. Please let us know if you have any questions and thank you for helping us! We are very excited to see what is created!

Target Market(s)

Female teens to early twenties

Coding

Coded - Design and coding required

Number of Pages Required

3 page

Font styles to use
Decorative
Script

Colors
cee9f5
85cae6
33a6d7
0393ce
cfdfed
85acd3

Requirements
Must have
• Online shopping/purchasing capabilities, dropdowns to select sizes for each item, easy to add/remove new or seasoned items.

```html
<!DOCTYPE html>
<html lang="en">
<head>
<meta charset="utf-8">
<title>Tavi Shirt Co. — Home</title>
<link href="https://fonts.googleapis.com/css2?family=Montserrat:ital,wght@0,300;0,400;0,500;0,600;0,700;0,800;0,900;1,700;1,800;1,900&display=swap" rel="stylesheet">
<style>
:root{
  --sky:#cee9f5;
  --powder:#85cae6;
  --blue:#33a6d7;
  --deep:#0393ce;
  --mist:#cfdfed;
  --steel:#85acd3;
  --ink:#1d2430;
  --text:#4a4f58;
  --muted:#8b929b;
  --white:#ffffff;
  --line:#e3e7ea;
}
*{box-sizing:border-box;margin:0;padding:0}
html,body{width:1200px;height:4560px;overflow:hidden}
body{font-family:"Montserrat",Arial,sans-serif;color:var(--text);background:var(--white);position:relative}
.photo{position:absolute}

/* hero */
.hero{position:absolute;left:0;top:0;width:1200px;height:680px;background:linear-gradient(120deg,#2fa6dc 0%,#3fb2e4 45%,#6cc5ec 100%);overflow:hidden}
.hero-shape{position:absolute;left:560px;top:-40px;width:700px;height:760px;background:rgba(255,255,255,.12);transform:skewX(-14deg)}
.brand-box{position:absolute;left:80px;top:0;width:260px;height:136px;background:var(--sky);display:flex;align-items:center;justify-content:center}
.brand-name{font-weight:700;font-size:24px;color:var(--deep);letter-spacing:1px}
.nav{position:absolute;right:60px;top:42px;display:flex;align-items:center;gap:28px;color:var(--white);font-size:14px;font-weight:600;letter-spacing:1px}
.hero-kicker{position:absolute;left:84px;top:206px;color:var(--white);font-style:italic;font-weight:700;font-size:34px;line-height:40px;letter-spacing:1px}
.hero-title{position:absolute;left:80px;top:246px;color:var(--white);font-style:italic;font-weight:900;font-size:98px;line-height:92px;letter-spacing:-2px}
.hero-copy{position:absolute;left:84px;top:446px;width:390px;color:var(--white);font-size:19px;line-height:1.25;font-weight:500}
.btn-shop{position:absolute;left:80px;top:560px;width:172px;height:52px;background:var(--deep);color:var(--white);font-size:14px;font-weight:700;letter-spacing:1px;display:flex;align-items:center;justify-content:center}
.hero-frame{position:absolute;left:620px;top:110px;width:490px;height:570px;border:2px solid rgba(255,255,255,.8)}
.hero-photo{left:560px;top:0;width:560px;height:680px;background:linear-gradient(180deg,#9fd6ee 0%,#cfe6f2 45%,#7bb4d8 100%)}
.slider{position:absolute;left:906px;top:632px;display:flex}
.slider span{width:48px;height:48px;display:flex;align-items:center;justify-content:center}
.slider .prev{background:var(--white)}
.slider .next{background:#1b1e24}

/* section titles */
.section-title{position:absolute;left:0;width:1200px;display:flex;align-items:center;justify-content:center;gap:34px;font-weight:700;font-size:26px;letter-spacing:3px;color:var(--ink)}
.section-title::before,.section-title::after{content:"";width:130px;height:2px;background:var(--powder)}

/* category */
.cat-card{position:absolute;top:848px;width:320px;height:452px}
.cat-card .photo{left:0;top:0;width:320px;height:400px}
.cat-label{position:absolute;left:56px;top:360px;width:208px;height:92px;background:var(--sky);display:flex;flex-direction:column;align-items:center;justify-content:center}
.cat-label b{font-size:28px;font-weight:600;color:var(--deep);letter-spacing:2px}
.cat-label small{font-size:14px;color:var(--text);margin-top:4px}

/* collection */
.coll-block{position:absolute;overflow:hidden}
.coll-word{position:absolute;color:var(--white);font-weight:500;font-size:62px;line-height:1.05;letter-spacing:6px}
.coll-sub{position:absolute;color:var(--white);font-size:13px}
.coll-arrow{position:absolute}
.coll-tag{position:absolute;background:var(--white);display:flex;flex-direction:column;justify-content:center;padding-left:60px}
.coll-tag-title{font-size:26px;font-weight:600;color:var(--ink);letter-spacing:1px;white-space:nowrap}
.coll-tag-title em{font-style:normal;color:var(--deep)}
.coll-tag svg{margin-top:12px}

/* products */
.prod{position:absolute;top:2428px;width:320px}
.prod-frame{width:320px;height:360px;background:var(--sky);position:relative}
.prod-frame .photo{left:56px;top:44px;width:208px;height:272px;background:linear-gradient(180deg,#f4f4f4,#dadde0);border:6px solid var(--white)}
.prod-name{margin-top:26px;text-align:center;font-size:14px;font-weight:600;color:var(--ink);letter-spacing:.5px}
.prod-price{margin-top:8px;text-align:center;font-size:30px;color:var(--blue)}
.pager{position:absolute;top:2928px;left:480px;display:flex;align-items:center;gap:18px;font-size:15px;color:var(--muted)}
.pager .all{border:2px solid #555;padding:6px 16px;color:var(--ink);margin-left:16px;font-weight:500}

/* promo */
.promo{position:absolute;left:0;top:3080px;width:1200px;height:340px}
.promo-photo{left:0;top:0;width:552px;height:340px;background:linear-gradient(135deg,#8aa37a 0%,#c9b89a 50%,#6d7f5e 100%)}
.promo-side{position:absolute;left:552px;top:0;width:648px;height:340px;background:linear-gradient(135deg,#3aa9d9,#1d8fc4)}
.promo-head{position:absolute;left:0;top:94px;width:648px;text-align:center;color:var(--white);font-size:32px;font-weight:600;letter-spacing:1px}
.promo-head b{font-weight:800}
.promo-sub{position:absolute;left:0;top:146px;width:648px;text-align:center;color:var(--sky);font-size:13px}
.promo-form{position:absolute;left:140px;top:186px;display:flex}
.promo-form .field{width:266px;height:40px;background:var(--white);font-size:13px;color:var(--muted);padding:11px 16px}
.promo-form .go{width:64px;height:40px;background:var(--powder);margin-left:8px;display:flex;align-items:center;justify-content:center}

/* news */
.news{position:absolute;top:3612px;width:320px}
.news .photo{left:0;top:0;width:320px;height:268px}
.news-date{position:absolute;left:80px;top:246px;width:160px;height:44px;background:var(--sky);font-size:13px;color:var(--ink);display:flex;align-items:center;justify-content:center}
.news-title{position:absolute;left:0;top:318px;width:320px;font-size:26px;font-weight:700;line-height:1.2;color:var(--ink)}
.news-text{position:absolute;left:0;top:412px;width:320px;font-size:13px;line-height:1.5;color:var(--muted)}
.news-more{position:absolute;left:0;top:496px;font-size:14px;color:var(--deep)}

/* footer */
.footer{position:absolute;left:0;top:4232px;width:1200px;height:328px;background:linear-gradient(90deg,#1590c8,#33a6d7)}
.foot-brand{position:absolute;left:80px;top:16px;width:194px;height:208px;background:var(--sky);display:flex;align-items:center;justify-content:center}
.foot-brand span{font-weight:700;font-size:18px;color:var(--deep)}
.foot-col{position:absolute;top:30px;color:var(--white)}
.foot-col h4{font-size:14px;font-weight:700;letter-spacing:1px;padding-bottom:14px;border-bottom:1px solid rgba(255,255,255,.5);margin-bottom:18px}
.foot-links{display:grid;grid-template-columns:130px 130px;row-gap:16px;font-size:14px}
.socials{position:absolute;left:1080px;top:30px;display:flex;flex-direction:column;gap:22px}
.socials span{width:22px;height:22px;border-radius:50%;background:var(--white);display:block}
.copyright{position:absolute;left:0;top:290px;width:1200px;text-align:center;font-size:13px;color:var(--sky)}
</style>
</head>
<body>

<section class="hero">
  <div class="hero-shape"></div>
  <div class="photo hero-photo" role="img" aria-label="Young woman in a denim jacket and white tee sitting and smiling"></div>
  <div class="hero-frame"></div>
  <div class="brand-box"><span class="brand-name">Tavi Shirt Co.</span></div>
  <nav class="nav">
    <svg width="20" height="20" viewBox="0 0 20 20" fill="none" stroke="#fff" stroke-width="2"><circle cx="8" cy="8" r="6"/><path d="M13 13l5 5"/></svg>
    <svg width="22" height="20" viewBox="0 0 22 20" fill="none" stroke="#fff" stroke-width="2"><path d="M1 2h4l3 11h10l2-8H6"/><circle cx="9" cy="17" r="1.5"/><circle cx="17" cy="17" r="1.5"/></svg>
    <span>LOGIN</span>
    <svg width="30" height="24" viewBox="0 0 30 24" fill="#fff"><rect y="0" width="30" height="4"/><rect y="10" width="30" height="4"/><rect y="20" width="30" height="4"/></svg>
  </nav>
  <div class="hero-kicker">SPECIAL OFFER</div>
  <h1 class="hero-title">FASHION<br>SALE</h1>
  <p class="hero-copy">Lorem ipsum dolor sit amet, consectetur adipiscing elit, sed do eiusmod tempor incididunt ut labore et dolore.</p>
  <a class="btn-shop">SHOP NOW</a>
  <div class="slider">
    <span class="prev"><svg width="20" height="14" viewBox="0 0 20 14" fill="none" stroke="#1b1e24" stroke-width="2"><path d="M19 7H2M7 1L1 7l6 6"/></svg></span>
    <span class="next"><svg width="20" height="14" viewBox="0 0 20 14" fill="none" stroke="#fff" stroke-width="2"><path d="M1 7h17M13 1l6 6-6 6"/></svg></span>
  </div>
</section>

<h2 class="section-title" style="top:776px">CATEGORY</h2>
<div class="cat-card" style="left:80px">
  <div class="photo" role="img" aria-label="Girl in sunglasses and a striped top" style="background:linear-gradient(160deg,#d9c4b0,#8f7f75)"></div>
  <div class="cat-label"><b>GIRL</b><small>collection</small></div>
</div>
<div class="cat-card" style="left:440px">
  <div class="photo" role="img" aria-label="Woman in a straw hat and floral dress" style="background:linear-gradient(160deg,#a8b0c4,#5b6c8c)"></div>
  <div class="cat-label"><b>LADY</b><small>collection</small></div>
</div>
<div class="cat-card" style="left:792px">
  <div class="photo" role="img" aria-label="Woman in a grey blazer on a city street" style="background:linear-gradient(160deg,#c9b8a6,#75706c)"></div>
  <div class="cat-label"><b>WOMEN</b><small>collection</small></div>
</div>

<h2 class="section-title" style="top:1432px">COLLECTION</h2>
<div class="coll-block" style="left:80px;top:1504px;width:512px;height:464px;background:var(--blue)">
  <div class="photo" role="img" aria-label="Woman in sunglasses and a plaid shirt" style="left:192px;top:0;width:320px;height:464px;background:linear-gradient(160deg,#e4e6e8,#8c9095)"></div>
  <div class="coll-word" style="left:36px;top:150px">CAS<br>UAL</div>
  <div class="coll-sub" style="left:60px;top:300px">collection</div>
  <svg class="coll-arrow" style="left:40px;top:330px" width="110" height="12" viewBox="0 0 110 12" fill="none" stroke="#fff" stroke-width="1.5"><path d="M0 6h106M100 1l6 5-6 5"/></svg>
</div>
<div class="coll-block" style="left:80px;top:1988px;width:512px;height:224px">
  <div class="photo" role="img" aria-label="Snowy forest scene" style="left:0;top:0;width:512px;height:224px;background:linear-gradient(180deg,#b9b7b2,#e8e8e6 60%,#9a9690)"></div>
  <div class="coll-tag" style="left:36px;top:36px;width:440px;height:152px;padding-left:92px">
    <div class="coll-tag-title">SUMMER <em>EDITION</em></div>
    <svg width="110" height="12" viewBox="0 0 110 12" fill="none" stroke="#33a6d7" stroke-width="1.5"><path d="M0 6h106M100 1l6 5-6 5"/></svg>
  </div>
</div>
<div class="coll-block" style="left:608px;top:1504px;width:504px;height:216px">
  <div class="photo" role="img" aria-label="Sandy beach under a pale sky" style="left:0;top:0;width:504px;height:216px;background:linear-gradient(180deg,#cfe3ee,#f0ebe3 60%,#d8c8b4)"></div>
  <div class="coll-tag" style="left:52px;top:36px;width:400px;height:144px;padding-left:84px">
    <div class="coll-tag-title">WINTER <em>EDITION</em></div>
    <svg width="110" height="12" viewBox="0 0 110 12" fill="none" stroke="#33a6d7" stroke-width="1.5"><path d="M0 6h106M100 1l6 5-6 5"/></svg>
  </div>
</div>
<div class="coll-block" style="left:608px;top:1744px;width:504px;height:468px;background:var(--blue)">
  <div class="photo" role="img" aria-label="Woman in a white formal blouse" style="left:192px;top:0;width:312px;height:468px;background:linear-gradient(160deg,#3a3c40,#1c1d20)"></div>
  <div class="coll-word" style="left:28px;top:140px">FOR<br>MAL</div>
  <div class="coll-sub" style="left:60px;top:292px">collection</div>
  <svg class="coll-arrow" style="left:36px;top:320px" width="110" height="12" viewBox="0 0 110 12" fill="none" stroke="#fff" stroke-width="1.5"><path d="M0 6h106M100 1l6 5-6 5"/></svg>
</div>

<h2 class="section-title" style="top:2360px">TOP PRODUCT</h2>
<div class="prod" style="left:80px">
  <div class="prod-frame"><div class="photo" role="img" aria-label="Model wearing a loose cream shirt and hat"></div></div>
  <div class="prod-name">BLUE NAVY BASIC T-SHIRT</div>
  <div class="prod-price">$ 19.90</div>
</div>
<div class="prod" style="left:440px">
  <div class="prod-frame"><div class="photo" role="img" aria-label="Model wearing a white blouse"></div></div>
  <div class="prod-name">SWEET PINK DRESS</div>
  <div class="prod-price">$ 19.90</div>
</div>
<div class="prod" style="left:792px">
  <div class="prod-frame"><div class="photo" role="img" aria-label="Model wearing a black dress"></div></div>
  <div class="prod-name">SUMMER HAT</div>
  <div class="prod-price">$ 19.90</div>
</div>
<div class="pager"><span style="color:var(--ink)">1</span><span>2</span><span>3</span><span>4</span><span class="all">See All</span></div>

<section class="promo">
  <div class="photo promo-photo" role="img" aria-label="Smiling woman in a black hat and leather jacket in a park"></div>
  <div class="promo-side">
    <div class="promo-head">GET A <b>20%</b> ON YOUR FIRST ORDER</div>
    <div class="promo-sub">Subscribe your email to get the latest news and offers</div>
    <div class="promo-form">
      <div class="field">your email</div>
      <div class="go"><svg width="20" height="12" viewBox="0 0 20 12" fill="none" stroke="#fff" stroke-width="1.5"><path d="M0 6h18M13 1l5 5-5 5"/></svg></div>
    </div>
  </div>
</section>

<h2 class="section-title" style="top:3544px">LATEST NEWS</h2>
<article class="news" style="left:80px">
  <div class="photo" role="img" aria-label="Two friends in autumn outfits" style="background:linear-gradient(160deg,#3d8fc2,#b0643f)"></div>
  <div class="news-date">March 12, 2020</div>
  <h3 class="news-title">Top 10 Fashion for this summer</h3>
  <p class="news-text">Fresh looks for warm days ahead, from light linen shirts to bright tees that pair well with denim and easy sandals.</p>
  <a class="news-more">Read more...</a>
</article>
<article class="news" style="left:440px">
  <div class="photo" role="img" aria-label="Woman in a beret and scarf" style="background:linear-gradient(160deg,#e9e6e2,#9b4a4a)"></div>
  <div class="news-date">June 11, 2020</div>
  <h3 class="news-title">Fashion week of Harbor Bay</h3>
  <p class="news-text">Highlights from the runway this season, with bold colours, relaxed cuts and layered tops shaping the next big trend.</p>
  <a class="news-more">Read more...</a>
</article>
<article class="news" style="left:792px">
  <div class="photo" role="img" aria-label="Group of friends laughing in sunglasses" style="background:linear-gradient(160deg,#d89a5e,#6fa0c9)"></div>
  <div class="news-date">June 23, 2020</div>
  <h3 class="news-title">Top 10 Fashion for this summer</h3>
  <p class="news-text">Our stylists pick their favourite shirts of the month and share simple tips to mix them into every weekend outfit.</p>
  <a class="news-more">Read more...</a>
</article>

<footer class="footer">
  <div class="foot-brand"><span>Tavi Shirt Co.</span></div>
  <div class="foot-col" style="left:336px;width:300px">
    <h4>HELP</h4>
    <div class="foot-links"><span>Payments</span><span>FAQ</span><span>Shipping</span><span>Contact us</span><span>Return</span><span>Store Locator</span></div>
  </div>
  <div class="foot-col" style="left:696px;width:300px">
    <h4>EXPLORE</h4>
    <div class="foot-links"><span>Categories</span><span>News</span><span>Trend</span><span>Privacy Policy</span><span>Shop</span><span>Terms &amp; Rights</span></div>
  </div>
  <div class="socials"><span></span><span></span><span></span><span></span></div>
  <div class="copyright">Copyright, your brand 2020</div>
</footer>

</body>
</html>
```